Ardent Summit contracting website

I need a website for my storm restoration/roofing contracting company. Looking for design that is in current style with professional details that aren't slammed together. i need something easy to edit my self to keep it fresh and up to date on current information and product. Website needs to have visible and easy to ready contents while keeping the modern, unique, specific, and high quality looks also easy to navigate between pages. My ideal targeted customer are more on the higher end simply due to the work being detailed and most the time custom and modern.

Website needs:

1. Services tab
Inspections - Drone Inspections with AI Damage detections with VOLTRA Software to inspect roofs after storms have impacted customer properties and also annual inspection roofs of every thing on the roof in minutes without having to climb roof manually leading to potential damage.

Residential - Roofing, Roof Repairs, Gutters, Siding, Paint, Decks, and Interior

Commerical - Roofing, Roof Coatings, Roof Maintenance Repair Plans, Roof Repairs, Roofing Gutters, Siding

Those are my most important services that i can think of right now, please set it how ever you think it needs to be set up for easy navigation.

2. Products
Ardent Summit doesn't look at a roof as just a roof. We look at the small details others may ignore or simply dont know anything about them. When we install a roof for clients/customer they are getting a full roofing system that includes only one manufacture per customer selection which qualities every roof installed for the highest material and labor warranty the top material manufactures offer. Ardent Summit carries the highest ranking Certifications with the leading manufacture so our customer can rest easy knowing their roofs were installed with precision.

Brands we love
Hollowbrook Crestline
RVN
Le Morvay

3. Gallery/Recent Projects

Link to sitelens or create folders or whatever for photos to be added weekly or bi weekly

4 . Service Area Map

5. About Us / The Ardent Summit Team

I do not have a domain yet looking for ideas on that as well. The website domain will also be used as the business email @'s

Files attached is the logos and business cards to get idea of the company colors and styles, open to whatever though and will consider everything if it catches my eye and is appealing.

Target Market(s)

Property owners, property management companies, maintenance managers for properties, home owners, business owners, land lords

Industry/Entity Type

Roofing contractor storm restoration home remodel

Coding

Coded - Design and coding required

Number of Pages Required

5+ page

Colors
EB3D1F
EC4F4E
F09395
F8D3D4
FCEDEE

Requirements
Must have
• Design like the RVN roofing manufacturer website or similar

```html
<!DOCTYPE html>
<html lang="en">
<head>
<meta charset="utf-8">
<title>Ardent Summit Contracting</title>
<link href="https://fonts.googleapis.com/css2?family=Orbitron:wght@700;800&family=Arimo:wght@400;700&family=Roboto:wght@500;700&display=swap" rel="stylesheet">
<style>
:root{
  --red:#ec1c24;
  --red-dark:#c8141b;
  --black:#000;
  --ink:#111;
  --text:#222;
  --muted:#6d6d6d;
  --light:#f2f2f2;
  --dark:#2a2a2a;
  --white:#fff;
  --line:#d4d4d4;
}
*{margin:0;padding:0;box-sizing:border-box}
html,body{width:1200px;height:5249px;overflow:hidden;background:var(--white)}
body{font-family:"Arimo",Arial,sans-serif;color:var(--text)}
.page{position:relative;width:1200px;height:5249px;overflow:hidden}
.abs{position:absolute}
.display{font-family:"Orbitron",sans-serif;font-weight:800;letter-spacing:2px;text-transform:uppercase}
.btn{position:absolute;display:flex;align-items:center;justify-content:center;background:var(--red);color:var(--white);font-family:"Roboto",sans-serif;font-weight:700;font-size:15px;text-transform:uppercase}
.mark{display:inline-block;width:22px;height:22px;background:var(--red);margin-right:12px;vertical-align:-2px}
.sec-title{position:absolute;font-family:"Orbitron",sans-serif;font-weight:800;font-size:31px;letter-spacing:2px;text-transform:uppercase;color:var(--ink);white-space:nowrap}
.center{left:0;width:1200px;text-align:center}
.fill{position:absolute}

/* header */
.site-header{position:absolute;left:0;top:0;width:1200px;height:137px;background:var(--black)}
.brand{position:absolute;left:126px;top:30px;color:var(--white);font-family:"Orbitron",sans-serif;font-weight:700;text-transform:uppercase;line-height:1;white-space:nowrap}
.brand .l1{font-size:25px;letter-spacing:1px}
.brand .l2{font-size:11px;letter-spacing:9.4px;margin-top:9px}
.call{position:absolute;left:705px;top:28px;font-family:"Roboto",sans-serif;font-weight:700;font-size:19px;color:var(--white);display:flex;align-items:center;gap:8px}
.call b{color:var(--red)}
.quote-top{position:absolute;left:931px;top:20px;width:138px;height:37px;border:2px solid var(--red);background:#1a1a1a;color:var(--white);font-family:"Roboto",sans-serif;font-weight:700;font-size:14px;display:flex;align-items:center;justify-content:center}
.nav a{position:absolute;top:86px;color:var(--white);font-family:"Roboto",sans-serif;font-weight:500;font-size:15px;text-decoration:none}

/* hero */
.hero{position:absolute;left:0;top:137px;width:1200px;height:613px;
  background:
    linear-gradient(90deg,rgba(0,0,0,0) 45%,rgba(0,0,0,.45) 100%),
    linear-gradient(165deg,#b8c3cc 0%,#a9adb0 22%,#7d6258 40%,#6b4b43 62%,#4f3a36 100%)}
.hero h1{position:absolute;left:676px;top:170px;color:var(--white);font-size:37px;line-height:41px}
.hero h1 span{color:var(--red)}

/* about */
.about{position:absolute;left:0;top:750px;width:1200px;height:578px;background:var(--light)}
.body-copy{position:absolute;font-size:14px;line-height:18px;color:var(--text)}

/* cards */
.svc-card{position:absolute;top:1487px;width:297px;height:412px;background:var(--white);border:1px solid #e0e0e0}
.svc-card .ph{height:240px}
.svc-card h3{margin-top:18px;text-align:center;font-family:"Orbitron",sans-serif;font-weight:700;font-size:22px;letter-spacing:2px;color:var(--ink);text-transform:uppercase}
.svc-card p{margin:18px auto 0;width:250px;text-align:center;font-size:14px;line-height:19px;color:var(--muted)}

/* why */
.why{position:absolute;left:0;top:2404px;width:1200px;height:607px;background:linear-gradient(180deg,#3a3633,#222 60%,#1b1b1b)}
.why-item{position:absolute;width:280px;color:var(--white)}
.why-item h4{font-family:"Roboto",sans-serif;font-weight:700;font-size:20px}
.why-item p{font-size:13.5px;line-height:17px;color:#bdbdbd;margin-top:4px}
.why-item.left{text-align:right}

/* projects */
.projects{position:absolute;left:0;top:3011px;width:1200px;height:611px;background:linear-gradient(180deg,#fff,#ececec)}
.proj-card{position:absolute;top:146px;width:295px;height:320px;background:var(--white);box-shadow:0 2px 8px rgba(0,0,0,.08)}
.proj-card .ph{height:210px}
.proj-card p{margin-top:30px;text-align:center;font-weight:700;font-size:19px;line-height:22px;color:var(--ink)}

/* service area */
.contact-row{position:absolute;left:126px;display:flex;gap:14px;font-size:14px;line-height:17px;color:var(--muted)}
.dot{width:32px;height:32px;border-radius:50%;background:var(--red);flex:none;display:flex;align-items:center;justify-content:center}
.area-map{position:absolute;left:621px;top:3732px;width:434px;height:393px;background:radial-gradient(ellipse at 50% 45%,#e2e2e2 0%,#d6d6d6 55%,#f6f6f6 85%,#fff 100%)}
.pin{position:absolute;width:18px;height:18px;border-radius:50%;background:var(--red);border:2px solid #fff;box-shadow:0 1px 3px rgba(0,0,0,.3)}
.pin.big{width:38px;height:38px;border:4px solid #fff}

/* quote */
.quote{position:absolute;left:0;top:4203px;width:1200px;height:615px;background:linear-gradient(135deg,#4b4e54 0%,#2f3238 40%,#3c4046 65%,#5e6a4d 100%)}
.quote-card{position:absolute;left:703px;top:89px;width:360px;height:454px;background:var(--white)}
.field{position:absolute;left:36px;width:292px;height:42px;border:1px solid var(--line);font-size:14px;color:#555;padding:12px 14px}

/* footer */
.site-footer{position:absolute;left:0;top:4818px;width:1200px;height:431px;background:var(--black);color:var(--white)}
.f-head{position:absolute;top:93px;font-family:"Orbitron",sans-serif;font-weight:700;font-size:15px;letter-spacing:1.5px;color:var(--red);text-transform:uppercase;white-space:nowrap}
.f-links a{position:absolute;left:397px;color:var(--white);font-size:14px;text-decoration:none}
.f-contact{position:absolute;left:556px;display:flex;align-items:center;gap:10px;font-size:14px;line-height:17px}
.ring{width:36px;height:36px;border:2px solid var(--white);border-radius:50%;flex:none;display:flex;align-items:center;justify-content:center}
.social{position:absolute;top:171px;width:33px;height:33px;border-radius:50%;background:var(--white)}
</style>
</head>
<body>
<div class="page">

  <header class="site-header">
    <div class="brand"><div class="l1">Ardent Summit</div><div class="l2">Contracting</div></div>
    <div class="call">
      <svg width="20" height="20" viewBox="0 0 24 24"><path fill="#ec1c24" d="M6.6 10.8a15.1 15.1 0 0 0 6.6 6.6l2.2-2.2a1 1 0 0 1 1-.25 11.4 11.4 0 0 0 3.6.57 1 1 0 0 1 1 1V20a1 1 0 0 1-1 1A17 17 0 0 1 3 4a1 1 0 0 1 1-1h3.5a1 1 0 0 1 1 1c0 1.25.2 2.45.57 3.57a1 1 0 0 1-.25 1z"/></svg>
      <span><b>Call:</b> 55 014 2290</span>
    </div>
    <div class="quote-top">GET A QUOTE</div>
    <nav class="nav">
      <a style="left:444px">SERVICES</a>
      <a style="left:562px">PRODUCTS</a>
      <a style="left:690px">GALLERY</a>
      <a style="left:811px">SERVICE AREA MAP</a>
      <a style="left:998px">ABOUT US</a>
    </nav>
  </header>

  <section class="hero" role="img" aria-label="Roofers working on a shingle roof beside a chimney">
    <h1 class="display">Welcome to<br>Ardent <span>Summit</span><br>Contracting</h1>
    <div class="btn" style="left:678px;top:321px;width:161px;height:49px">Get a quote</div>
  </section>

  <section class="about">
    <h2 class="sec-title" style="left:126px;top:114px"><span class="mark"></span>About us</h2>
    <p class="body-copy" style="left:126px;top:177px;width:430px">Lorem ipsum dolor sit amet, consectetur adipiscing elit, sed do eiusmod tempor incididunt ut labore et dolore magna aliqua. Quis ipsum suspendisse ultrices gravida. Risus commodo viverra maecenas accumsan lacus vel facilisis.<br><br>Lorem ipsum dolor sit amet, consectetur adipiscing elit, sed do eiusmod tempor incididunt ut labore et dolore magna aliqua. Quis ipsum suspendisse ultrices gravida. Risus commodo viverra maecenas accumsan lacus vel facilisis. Quis ipsum suspendisse ultrices gravida. Risus commodo viverra maecenas accumsan lacus vel facilisis.</p>
    <div class="btn" style="left:126px;top:397px;width:145px;height:55px">Read more</div>
    <svg class="abs" style="left:564px;top:81px" width="636" height="414" viewBox="0 0 636 414">
      <polygon points="173,0 193,0 20,414 0,414" fill="#ec1c24"/>
      <defs><linearGradient id="ag" x1="0" y1="0" x2="1" y2="1"><stop offset="0" stop-color="#cdd8df"/><stop offset=".35" stop-color="#9aa3a8"/><stop offset=".6" stop-color="#6e6c6a"/><stop offset="1" stop-color="#3e3a37"/></linearGradient></defs>
      <polygon points="203,0 636,0 636,414 30,414" fill="url(#ag)" role="img" aria-label="Two roofers in hard hats installing shingles"/>
    </svg>
  </section>

  <section>
    <h2 class="sec-title center" style="top:1408px"><span class="mark"></span>Services</h2>
    <article class="svc-card" style="left:122px"><div class="ph" role="img" aria-label="Roofer inspecting a shingle roof" style="background:linear-gradient(180deg,#5b86c4 0%,#8aa6c8 30%,#7d6a5a 55%,#5d4d42 100%)"></div><h3>Inspections</h3><p>Lorem ipsum dolor sit amet, consectetur adipiscing elitseo eiusmod tempor inciore</p></article>
    <article class="svc-card" style="left:452px"><div class="ph" role="img" aria-label="Residential house roofline with siding" style="background:linear-gradient(180deg,#d7dde0 0%,#6a5d52 35%,#8c7a62 70%,#6d5f4e 100%)"></div><h3>Residential</h3><p>Lorem ipsum dolor sit amet, consectetur adipiscing elitseo eiusmod tempor inciore</p></article>
    <article class="svc-card" style="left:776px"><div class="ph" role="img" aria-label="Roofer in safety vest working on a commercial roof" style="background:linear-gradient(180deg,#7ea7d4 0%,#9bb5d2 25%,#6f6f72 45%,#4c4c50 100%)"></div><h3>Commercial</h3><p>Lorem ipsum dolor sit amet, consectetur adipiscing elitseo eiusmod tempor inciore</p></article>
  </section>

  <section>
    <svg class="abs" style="left:0;top:2006px" width="1200" height="398" viewBox="0 0 1200 398">
      <defs><linearGradient id="pg" x1="0" y1="0" x2="1" y2="1"><stop offset="0" stop-color="#5f6a45"/><stop offset=".45" stop-color="#8b8a7e"/><stop offset=".7" stop-color="#b59a3a"/><stop offset="1" stop-color="#4e4e52"/></linearGradient></defs>
      <rect width="600" height="398" fill="url(#pg)" role="img" aria-label="Roofer using a nail gun on shingles"/>
      <polygon points="550,0 1200,0 1200,398 373,398" fill="#fff"/>
      <polygon points="564,0 1200,0 1200,398 387,398" fill="#ec1c24"/>
    </svg>
    <h2 class="sec-title" style="left:621px;top:2104px;color:#fff"><span class="mark" style="background:#fff"></span>Products</h2>
    <p class="body-copy" style="left:626px;top:2168px;width:430px;color:#fff">Lorem ipsum dolor sit amet, consectetur adipiscing elit, sed do eiusmod tempor incididunt ut labore et dolore magna aliqua. Quis ipsum suspendisse ultrices gravida. Risus commodo viverra maecenas accumsan lacus vel facilisis.</p>
    <div class="btn" style="left:623px;top:2263px;width:125px;height:49px;background:transparent;border:2px solid #fff">Call now</div>
  </section>

  <section class="why">
    <h2 class="sec-title center" style="top:100px;color:#fff"><span class="mark"></span>Why choose us?</h2>
    <div class="abs" style="left:456px;top:215px;width:286px;height:286px;border-radius:50%;border:7px solid var(--red);background:#3a3a3a;display:flex;align-items:center;justify-content:center;text-align:center;color:#fff;font-family:'Orbitron',sans-serif;font-weight:800;font-size:24px;line-height:30px">ARDENT<br>SUMMIT</div>
    <div class="why-item left" style="left:62px;top:206px"><h4>Consectetu ipisc</h4><p>Lorem ipsum dolor sit amet, consec adipiscing elit, sed do eiusmod tempor incididunt ut labore et dolore.</p></div>
    <div class="why-item left" style="left:62px;top:373px"><h4>Consectetu ipisc</h4><p>Lorem ipsum dolor sit amet, consec adipiscing elit, sed do eiusmod tempor incididunt ut labore et dolore.</p></div>
    <div class="why-item" style="left:862px;top:206px"><h4>Consectetu ipisc</h4><p>Lorem ipsum dolor sit amet, consec adipiscing elit, sed do eiusmod tempor incididunt ut labore et dolore.</p></div>
    <div class="why-item" style="left:862px;top:373px"><h4>Consectetu ipisc</h4><p>Lorem ipsum dolor sit amet, consec adipiscing elit, sed do eiusmod tempor incididunt ut labore et dolore.</p></div>
    <svg class="abs" style="left:366px;top:214px" width="76" height="60" viewBox="0 0 76 60" fill="none" stroke="#fff" stroke-width="2.5"><rect x="6" y="16" width="62" height="36" rx="3"/><path d="M12 16 L22 4 L70 22"/><circle cx="37" cy="34" r="8" stroke="#ec1c24"/></svg>
    <svg class="abs" style="left:363px;top:380px" width="76" height="68" viewBox="0 0 76 68" fill="none" stroke="#fff" stroke-width="2.5"><circle cx="42" cy="38" r="22"/><path d="M42 24v14l9 6" stroke="#ec1c24"/><path d="M36 10h12M42 10v6"/><path d="M4 30h12M2 40h12M6 50h12"/></svg>
    <svg class="abs" style="left:762px;top:208px" width="76" height="76" viewBox="0 0 76 76" fill="none" stroke="#fff" stroke-width="2.5"><path d="M12 8v60M24 8v60M8 8h20"/><circle cx="52" cy="28" r="10" stroke="#ec1c24"/><circle cx="52" cy="28" r="4"/><circle cx="48" cy="56" r="8" stroke="#ec1c24"/></svg>
    <svg class="abs" style="left:764px;top:376px" width="76" height="70" viewBox="0 0 76 70" fill="none" stroke="#fff" stroke-width="2.5"><path d="M6 62 L20 28 L70 28 L58 62 Z"/><path d="M14 45h52M30 28l-8 34M46 28l-8 34"/><rect x="50" y="6" width="10" height="16" stroke="#ec1c24"/></svg>
  </section>

  <section class="projects">
    <h2 class="sec-title center" style="top:68px"><span class="mark"></span>Recent projects</h2>
    <article class="proj-card" style="left:126px"><div class="ph" role="img" aria-label="Aerial view of homes with rooftop solar panels" style="background:linear-gradient(180deg,#8fb0cc 0%,#6d6a66 30%,#5b4c3e 60%,#3c4a34 100%)"></div><p>Lorem ipsum dolor sit<br>ameconsect.</p></article>
    <article class="proj-card" style="left:450px"><div class="ph" role="img" aria-label="Roofer nailing new shingles" style="background:linear-gradient(160deg,#6b7552 0%,#a89a5a 30%,#8d8b86 55%,#5a5a5e 100%)"></div><p>Lorem ipsum dolor sit<br>ameconsect.</p></article>
    <article class="proj-card" style="left:774px"><div class="ph" role="img" aria-label="Stone house with new shingle roof" style="background:linear-gradient(160deg,#2f6fc4 0%,#6f7680 40%,#8b7860 75%,#6a6a6a 100%)"></div><p>Lorem ipsum dolor sit<br>ameconsect.</p></article>
    <div class="btn" style="left:528px;top:497px;width:144px;height:49px">View all</div>
  </section>

  <section>
    <h2 class="sec-title" style="left:126px;top:3726px"><span class="mark"></span>Service area</h2>
    <p class="body-copy" style="left:126px;top:3800px;width:410px">Lorem ipsum dolor sit amet, consectetur adipiscing elit, sed do eiusmod tempor incididunt ut labore et dolore magna aliqua. Quis ipsum suspendisse ultrices gravida.</p>
    <div class="abs" style="left:126px;top:3886px;font-family:'Roboto',sans-serif;font-weight:700;font-size:17px;color:#555">SERVICE AREA 1</div>
    <div class="contact-row" style="top:3926px"><span class="dot"><svg width="14" height="18" viewBox="0 0 14 18"><path fill="#fff" d="M7 0a7 7 0 0 0-7 7c0 5 7 11 7 11s7-6 7-11a7 7 0 0 0-7-7zm0 9.5A2.5 2.5 0 1 1 7 4.5a2.5 2.5 0 0 1 0 5z"/></svg></span><span>Address Lorem ipsum dumy 67<br>dumy street name 45</span></div>
    <div class="contact-row" style="top:3977px"><span class="dot"><svg width="16" height="16" viewBox="0 0 24 24"><path fill="#fff" d="M6.6 10.8a15.1 15.1 0 0 0 6.6 6.6l2.2-2.2a1 1 0 0 1 1-.25 11.4 11.4 0 0 0 3.6.57 1 1 0 0 1 1 1V20a1 1 0 0 1-1 1A17 17 0 0 1 3 4a1 1 0 0 1 1-1h3.5a1 1 0 0 1 1 1c0 1.25.2 2.45.57 3.57a1 1 0 0 1-.25 1z"/></svg></span><span>Phone:<br>555 208 316</span></div>
    <div class="contact-row" style="top:4026px"><span class="dot"><svg width="16" height="12" viewBox="0 0 16 12"><rect width="16" height="12" rx="1" fill="#fff"/><path d="M1 1l7 5 7-5" stroke="#ec1c24" stroke-width="1.5" fill="none"/></svg></span><span>Email us:<br>hello@ardentsummit.example</span></div>
    <div class="area-map" role="img" aria-label="Map of the service region with location markers"></div>
    <span class="pin" style="left:766px;top:3826px"></span>
    <span class="pin" style="left:848px;top:3857px"></span>
    <span class="pin" style="left:664px;top:3891px"></span>
    <span class="pin" style="left:960px;top:3904px"></span>
    <span class="pin big" style="left:838px;top:3945px"></span>
    <span class="pin" style="left:966px;top:4010px"></span>
  </section>

  <section class="quote" role="img" aria-label="Workers installing solar panels on a metal roof">
    <div class="quote-card">
      <div class="abs display" style="left:0;top:44px;width:360px;text-align:center;font-size:23px;color:var(--ink)">Get a quote</div>
      <div class="field" style="top:100px">Name</div>
      <div class="field" style="top:155px">Email:</div>
      <div class="field" style="top:212px">Phone:</div>
      <div class="field" style="top:267px;height:120px">Message:</div>
      <div class="btn" style="left:126px;top:369px;width:114px;height:36px">Submit</div>
    </div>
  </section>

  <footer class="site-footer">
    <div class="brand" style="top:86px;left:128px"><div class="l1" style="font-size:20px">Ardent Summit</div><div class="l2" style="font-size:10px;letter-spacing:7.2px;margin-top:7px">Contracting</div></div>
    <span class="social" style="left:144px" aria-label="Social profile"></span>
    <span class="social" style="left:189px" aria-label="Social profile"></span>
    <span class="social" style="left:234px" aria-label="Social profile"></span>
    <span class="social" style="left:279px" aria-label="Social profile"></span>

    <div class="f-head" style="left:397px">Links</div>
    <nav class="f-links">
      <a style="top:136px">About</a><a style="top:163px">Services</a><a style="top:190px">Products</a><a style="top:217px">Recent Projects</a><a style="top:244px">Service Area Map</a><a style="top:271px">About Us</a>
    </nav>

    <div class="f-head" style="left:560px">Contact us</div>
    <div class="f-contact" style="top:140px"><span class="ring"><svg width="14" height="18" viewBox="0 0 14 18"><path fill="#fff" d="M7 0a7 7 0 0 0-7 7c0 5 7 11 7 11s7-6 7-11a7 7 0 0 0-7-7zm0 9.5A2.5 2.5 0 1 1 7 4.5a2.5 2.5 0 0 1 0 5z"/></svg></span><span>Location Name<br>Dummy address livv<br>Halden 6425 PE (2004)</span></div>
    <div class="f-contact" style="top:206px"><span class="ring"><svg width="16" height="16" viewBox="0 0 24 24"><path fill="#fff" d="M6.6 10.8a15.1 15.1 0 0 0 6.6 6.6l2.2-2.2a1 1 0 0 1 1-.25 11.4 11.4 0 0 0 3.6.57 1 1 0 0 1 1 1V20a1 1 0 0 1-1 1A17 17 0 0 1 3 4a1 1 0 0 1 1-1h3.5a1 1 0 0 1 1 1c0 1.25.2 2.45.57 3.57a1 1 0 0 1-.25 1z"/></svg></span><span>Phone:555.013.0447</span></div>
    <div class="f-contact" style="top:257px"><span class="ring"><svg width="16" height="12" viewBox="0 0 16 12"><rect width="16" height="12" rx="1" fill="#fff"/><path d="M1 1l7 5 7-5" stroke="#000" stroke-width="1.5" fill="none"/></svg></span><span>office@ardentsummit.example</span></div>

    <div class="f-head" style="left:815px">Newsletter sign up</div>
    <p class="abs" style="left:815px;top:138px;width:250px;font-size:14px;line-height:17px">Lorem ipsum dolor sit amelor conse ctet ur adipisclorem ipsumilited do eiusmod tempor incididu.</p>
    <div class="abs" style="left:815px;top:209px;width:240px;height:49px;background:#fff;color:#888;font-size:14px;padding:16px 14px">Email</div>
    <svg class="abs" style="left:1005px;top:227px" width="34" height="14" viewBox="0 0 34 14"><path d="M0 7h32M26 1l6 6-6 6" stroke="#222" stroke-width="1.6" fill="none"/></svg>

    <div class="abs" style="left:98px;top:360px;width:955px;height:1px;background:#444"></div>
    <div class="abs center" style="top:380px;font-size:13px">© 2023 All Rights Reserved.Terms &amp; Conditions Privacy Policy</div>
  </footer>

</div>
</body>
</html>
```